Redesign digital storytelling app interface for picking topics and recording/listening to audio

We are building an app for users to tell stories to their friends and family in response to prompts. Our current interface is very basic, and we want to have it redesigned in order to make it more visually appealing and feel more like a comfortable conversation. We also need one screen created from scratch to match the existing screens.
In this app, the user picks a story topic from a list a friend has sent to them and then makes an audio recording in response to that topic. The other user receives the recording and listens to it, then responds to the story.
Attached are images of the screens we want to have redesigned.
1. Topic Selection Screen - screen showing the three prompts that the user will pick from before recording their story.
2. Story Recording Screen - screen that the user sees while recording their story.
3. Playback Screen - screen that the user sees while listening to the story.
4. Respond to Story Screen - screen that the user sees after listening to the story on the playback screen. This screen should have buttons for the user to communicate with the person who sent them the story, including: a quick record button where the user can send a voice message responding to the story, a phone call button, a text button, a velnorix button, and a drumo button. It should also have a button to return to the main menu.
I've also attached a graphic showing what we are currently using for a logo and color scheme. This does not need to be followed exactly.
As an added bonus, please give an example of how to manage these screens when the stories are not one-on-one, but in a group of four people.
The mood of this product should be comfortable, personal, and conversational. We want people to feel like they're chatting with an old friend. The design itself can be anything at all, so go wild!
Digital

```html
<!DOCTYPE html>
<html lang="en">
<head>
<meta charset="utf-8">
<title>Hear a Story</title>
<link href="https://fonts.googleapis.com/css2?family=Roboto:wght@400;500&family=Open+Sans:wght@600&display=swap" rel="stylesheet">
<style>
  :root {
    --status-pink: #d81b60;
    --bar-pink: #e91e63;
    --page-bg: #eff3f6;
    --card-bg: #ffffff;
    --text-dark: #555555;
    --text-muted: #7a7a7a;
    --wave-line: #f080a8;
    --wave-fill: #fbf0f4;
    --progress: #22b35e;
    --track: #cccccc;
    --icon: #666666;
    --avatar: #a7a39c;
  }
  * { margin: 0; padding: 0; box-sizing: border-box; }
  html, body { width: 675px; height: 1200px; overflow: hidden; }
  body {
    position: relative;
    background: var(--page-bg);
    font-family: "Roboto", Arial, sans-serif;
  }
  .status-bar {
    position: absolute; left: 0; top: 0; width: 675px; height: 45px;
    background: var(--status-pink);
  }
  .status-bar .clock {
    position: absolute; left: 596px; top: 8px;
    color: #fff; font-size: 24px; line-height: 28px;
  }
  .status-bar svg { position: absolute; left: 0; top: 0; }
  .app-bar {
    position: absolute; left: 0; top: 45px; width: 675px; height: 105px;
    background: var(--bar-pink);
    box-shadow: 0 2px 4px rgba(0,0,0,0.18);
    display: flex; align-items: center; justify-content: center;
  }
  .app-bar h1 {
    color: #fff; font-weight: 400; font-size: 35px; margin-top: 2px;
  }
  .card {
    position: absolute; left: 21px; width: 637px;
    background: var(--card-bg);
    box-shadow: 0 1px 3px rgba(0,0,0,0.2);
  }
  .prompt-card { top: 174px; height: 178px; }
  .avatar {
    position: absolute; left: 26px; top: 38px; width: 93px; height: 93px;
    border-radius: 50%;
    background: radial-gradient(circle at 50% 40%, #c9c3b8, var(--avatar) 60%, #6f8aa6);
  }
  .sender-name {
    position: absolute; left: 150px; top: 42px;
    font-size: 30px; color: var(--text-dark); font-weight: 400;
  }
  .prompt-text {
    position: absolute; left: 147px; top: 87px; width: 450px;
    font-size: 21.5px; line-height: 27px; color: var(--text-muted);
  }
  .player-card { top: 376px; height: 806px; overflow: hidden; }
  .waveform { position: absolute; left: 0; top: 0; }
  .timer {
    position: absolute; left: 0; width: 637px; top: 478px;
    text-align: center;
    font-family: "Open Sans", Arial, sans-serif; font-weight: 600;
    font-size: 43px; letter-spacing: 2px; color: var(--text-dark);
  }
  .seek { position: absolute; left: 52px; top: 607px; overflow: visible; }
  .controls { position: absolute; left: 0; top: 710px; }
</style>
</head>
<body>
  <div class="status-bar">
    <svg width="675" height="45" aria-hidden="true">
      <polygon points="524,34 546,11 546,34" fill="#ffffff" opacity="0.55"/>
      <polygon points="524,34 538,20 538,34" fill="#ffffff"/>
      <rect x="569" y="10" width="9" height="3" fill="#ffffff" opacity="0.55"/>
      <rect x="566" y="13" width="15" height="21" rx="1.5" fill="#ffffff" opacity="0.55"/>
      <rect x="566" y="23" width="15" height="11" rx="1.5" fill="#ffffff"/>
    </svg>
    <span class="clock">12:30</span>
  </div>

  <header class="app-bar"><h1>Hear a Story</h1></header>

  <section class="card prompt-card">
    <div class="avatar" role="img" aria-label="Profile photo of the storyteller"></div>
    <h2 class="sender-name">Owen Castellan</h2>
    <p class="prompt-text">Who was your first roommate? Are you still friends?</p>
  </section>

  <section class="card player-card">
    <svg class="waveform" width="637" height="406" aria-hidden="true">
      <polygon fill="var(--wave-fill)" points="0,320 32,308 64,314 96,296 128,280 160,288 192,272 224,260 256,274 288,292 320,284 352,266 384,248 416,256 448,240 480,262 512,286 544,278 576,300 608,292 637,310 637,406 0,406"/>
      <polyline fill="none" stroke="var(--wave-line)" stroke-width="3" stroke-linejoin="round" points="0,320 32,308 64,314 96,296 128,280 160,288 192,272 224,260 256,274 288,292 320,284 352,266 384,248 416,256 448,240 480,262 512,286 544,278 576,300 608,292 637,310"/>
    </svg>

    <div class="timer">00:01:26</div>

    <svg class="seek" width="540" height="50" aria-label="Playback position">
      <line x1="2" y1="22" x2="520" y2="22" stroke="var(--track)" stroke-width="5" stroke-linecap="round"/>
      <line x1="2" y1="22" x2="273" y2="22" stroke="var(--progress)" stroke-width="5" stroke-linecap="round"/>
      <circle cx="294" cy="25" r="22" fill="rgba(0,0,0,0.12)"/>
      <circle cx="294" cy="22" r="22" fill="#ffffff" stroke="#e2e2e2" stroke-width="1"/>
    </svg>

    <svg class="controls" width="637" height="60" aria-label="Playback controls">
      <g fill="var(--icon)">
        <polygon points="143,26 165,12 165,40"/>
        <polygon points="165,26 187,12 187,40"/>
        <rect x="297" y="7" width="11" height="38"/>
        <rect x="317" y="7" width="11" height="38"/>
        <polygon points="438,12 460,26 438,40"/>
        <polygon points="460,12 482,26 460,40"/>
      </g>
    </svg>
  </section>
</body>
</html>
```